Connected Building Infrastructure Business needs awesome document templates.

We'd like to have a fresh set of document templates for business letters, documents, and power point presentations. Tamarind Wiring and Safety works with IT teams, construction firms, and consultants to provide structured cabling, electronic security, and connected building infrastructure services to firms through the state of New York, Massachusetts, and Vermont.

We have recently refreshed our logo and have started some branding and would like to continue the themes already in place. As a result of this project we are looking for

-letter head template
-document template for sales material (contracts and proposals)
-document template for customer documentation and hand outs
-PowerPoint template for customer and internal presentations

Target Market(s)

CIOs, Vice President of IT Facilities, and Security, Small/Medium Size Business Owners, General Contractors

Industry/Entity Type

Business

Font styles to use
Sans Serif

Requirements
Must have
• -letter head template
• -document template for sales material (contracts and proposals)
• -document template for customer documentation and hand outs
• -PowerPoint template for customer and internal presentations
Should not have
• Do not change logo. Can use knockout and/or black and white version of logo if needed.

```html
<!DOCTYPE html>
<html lang="en">
<head>
<meta charset="utf-8">
<title>Tamarind Wiring and Safety — Letterhead</title>
<link href="https://fonts.googleapis.com/css2?family=Open+Sans:wght@400;600;700&display=swap" rel="stylesheet">
<style>
  :root {
    --backdrop: #e4e4e4;
    --paper: #ffffff;
    --ink: #2b2b2b;
    --ink-soft: #555555;
    --brand-black: #0d0d0d;
    --brand-green: #0f6b45;
  }
  html, body {
    margin: 0;
    padding: 0;
    width: 1200px;
    height: 1200px;
    overflow: hidden;
    background: var(--backdrop);
    font-family: "Open Sans", Arial, sans-serif;
  }
  .letterhead {
    position: absolute;
    left: 204px;
    top: 40px;
    width: 792px;
    height: 1120px;
    background: var(--paper);
    box-shadow: 0 4px 18px rgba(0,0,0,0.12);
    overflow: hidden;
    color: var(--ink);
  }
  .brand {
    position: absolute;
    left: 64px;
    top: 70px;
    display: flex;
    align-items: center;
    gap: 10px;
  }
  .brand-square {
    width: 16px;
    height: 16px;
    background: var(--brand-green);
  }
  .brand-name {
    font-size: 17px;
    font-weight: 700;
    letter-spacing: 0.5px;
    text-transform: uppercase;
    color: var(--brand-black);
  }
  .contact {
    position: absolute;
    right: 64px;
    top: 62px;
    font-size: 10.5px;
    line-height: 1.55;
    color: var(--ink);
  }
  .contact-line {
    display: flex;
    align-items: center;
    gap: 6px;
  }
  .contact-line svg { width: 10px; height: 10px; fill: var(--brand-green); }
  .letter-body {
    position: absolute;
    left: 64px;
    top: 200px;
    width: 600px;
    font-size: 13.5px;
    line-height: 1.75;
  }
  .salutation { margin: 0 0 22px; font-size: 14.5px; }
  .letter-body p.paragraph { margin: 0 0 26px; }
  .signature-area {
    width: 120px;
    height: 44px;
    margin-top: 40px;
    background: linear-gradient(90deg, rgba(0,0,0,0.06), rgba(0,0,0,0.02));
  }
  .signer-name { margin: 10px 0 0; font-size: 19px; color: var(--ink); }
  .signer-title { margin: 2px 0 0; font-size: 13px; color: var(--ink-soft); }
  .footer-wave {
    position: absolute;
    left: 0;
    bottom: 0;
    width: 792px;
    height: 520px;
  }
</style>
</head>
<body>
  <main class="letterhead">
    <header>
      <div class="brand">
        <span class="brand-square"></span>
        <span class="brand-name">Tamarind Wiring and Safety</span>
      </div>
      <div class="contact">
        <div>48 Larchmont Way,</div>
        <div>Saratoga, NY 12866</div>
        <div class="contact-line">
          <svg viewBox="0 0 24 24"><path d="M6.6 10.8a15 15 0 0 0 6.6 6.6l2.2-2.2c.3-.3.7-.4 1-.2 1.1.4 2.3.6 3.6.6.6 0 1 .4 1 1V20c0 .6-.4 1-1 1A17 17 0 0 1 3 4c0-.6.4-1 1-1h3.5c.6 0 1 .4 1 1 0 1.3.2 2.5.6 3.6.1.3 0 .7-.2 1z"/></svg>
          (518) 555 0142
        </div>
        <div class="contact-line">
          <svg viewBox="0 0 24 24"><circle cx="12" cy="12" r="10"/></svg>
          www.tamarindwiring.com
        </div>
      </div>
    </header>

    <section class="letter-body">
      <p class="salutation">Dear Mr. Carver,</p>
      <p class="paragraph">Lorem ipsum dolor sit amet, consectetur adipiscing elit. Donec orci purus, luctus vitae dignissim eu, iaculis sed purus. Vivamus faucibus, ipsum nec aliquet viverra, leo mauris condimentum ligula, sit amet sagittis enim ligula quis arcu. Nam egestas tortor id nisi porttitor mattis. In tortor ante, ultricies in suscipit a, tempus non massa. Vivamus et auctor mi. Fusce vel massa nulla. Phasellus nec eros mauris, et scelerisque orci. Donec malesuada orci vitae nulla accumsan porta a id massa. Quisque accumsan iaculis magna sit amet fringilla. Maecenas consequat, magna eget tincidunt semper, odio nibh rutrum mi, id feugiat ante nisi eu risus. Vestibulum nunc orci, rhoncus a placerat in, ultricies in mi. Cras mattis varius eros, vel fringilla nisi suscipit eget.</p>
      <p class="paragraph">Quisque scelerisque sagittis nulla at porttitor. Mauris a justo et tellus interdum tristique. Sed id augue vitae urna euismod commodo aliquet a quam. Pellentesque arcu velit, cursus et malesuada ut, consequat et diam. Nullam erat sem, rhoncus id ullamcorper vitae, rhoncus et arcu. In ultricies ultricies nulla, ut rutrum nisi iaculis at. Donec eu magna a metus ornare faucibus. Fusce aliquet faucibus ultricies. Morbi semper, est id tincidunt gravida, sem arcu adipiscing lacus, ac bibendum nulla leo eu purus. Quisque nec diam sed risus consectetur accumsan quis nibh. Vestibulum id purus lorem.</p>
      <div class="signature-area" role="img" aria-label="Handwritten signature of the sender"></div>
      <p class="signer-name">Jordan Hale</p>
      <p class="signer-title">Co-Founder &amp; CEO</p>
    </section>

    <svg class="footer-wave" viewBox="0 0 792 520" preserveAspectRatio="none" aria-hidden="true">
      <path d="M0,520 L0,478 C260,470 560,340 792,60 L792,520 Z" fill="var(--brand-black)"/>
      <path d="M0,462 C200,440 420,400 560,300 C470,372 250,440 0,474 Z" fill="var(--brand-green)"/>
    </svg>
  </main>
</body>
</html>
```